Heart Rate Game Display Graphic

We need a unique layout / info-graphic for our heart rate software to display an individuals hear rate, HR%, and other data together within a larger class of up to 40 other users. Graphics should be colorful, dynamic, and intuitive.

Target Market(s)

Group Fitness Classes

Font styles to use
Sans Serif

Colors

Designer to choose colors to be used in the design.

Requirements
Must have
• Individual Box must contain data field or graphic representation of:
• User Name
• Heart Rate %
• Points Earned / % Accuracy
Nice to have
• thinking other shape design that easily integrates with 40+ of the same shape. Looking for depth of design and or some 3d visualizations. Competing companies:
• https://www.pulsekite.org/
• https://www.gorvo.com/
• https://www.trevank.com/us-en/club
• https://vumbralo.com/
• https://kelvaro.fit/personal-trainer/
• https://www.dashoply.io/Solutions/Heart-Rate-Training
• http://nuvo.bramfieldsystems.com/
• https://lomi-wheel.com/explore/lomi-wheel-indoor-cycling-app/
Should not have
• should NOT be just be plain squares representing each client.

```html
<!DOCTYPE html>
<html lang="en">
<head>
<meta charset="utf-8">
<title>Heart Rate Class Board</title>
<link rel="stylesheet" href="https://fonts.googleapis.com/css2?family=Bebas+Neue&display=swap">
<style>
  :root {
    --board: #232f4a;
    --dial: #ffffff;
    --heart: #c0274d;
    --heart-edge: #e0567a;
    --ink: #ffffff;
    --purple: #8e4fa3;
    --green: #8fbc2b;
    --orange: #f5a425;
    --blue: #3578a8;
    --pink: #f52d66;
  }
  * { margin: 0; padding: 0; box-sizing: border-box; }
  html, body { width: 1200px; height: 660px; overflow: hidden; background: var(--board); }
  .board {
    position: relative;
    width: 1200px;
    height: 660px;
    padding: 33px 0 0 45px;
    display: grid;
    grid-template-columns: repeat(7, 158.5px);
    grid-auto-rows: 181px;
    row-gap: 25px;
    font-family: "Bebas Neue", "Oswald", sans-serif;
    color: var(--ink);
  }
  .player { display: flex; flex-direction: column; align-items: center; }
  .player__name {
    height: 30px;
    line-height: 30px;
    font-size: 24px;
    letter-spacing: 1.5px;
  }
  .player__dial { width: 151px; height: 151px; display: block; }
  .dial__face { fill: var(--dial); }
  .dial__level, .dial__badge { fill: var(--tone); }
  .dial__heart { fill: var(--heart); stroke: var(--heart-edge); stroke-width: 1.2; }
  .dial__text {
    fill: var(--ink);
    font-family: "Bebas Neue", "Oswald", sans-serif;
    text-anchor: middle;
    dominant-baseline: central;
  }
  .dial__pct { font-size: 17px; }
  .dial__bpm { font-size: 16px; }
  .tone-purple { --tone: var(--purple); }
  .tone-green { --tone: var(--green); }
  .tone-orange { --tone: var(--orange); }
  .tone-blue { --tone: var(--blue); }
  .tone-pink { --tone: var(--pink); }
  .defs { position: absolute; width: 0; height: 0; }
</style>
</head>
<body>
<svg class="defs" aria-hidden="true">
  <defs>
    <clipPath id="bowl"><circle cx="0" cy="0" r="45"/></clipPath>
    <symbol id="heart" viewBox="-17 -16 34 31">
      <path d="M0 13 C-6 8 -16 2 -16 -5 C-16 -11 -11 -15 -6 -15 C-3 -15 -1 -13 0 -11 C1 -13 3 -15 6 -15 C11 -15 16 -11 16 -5 C16 2 6 8 0 13Z"/>
    </symbol>
  </defs>
</svg>

<main class="board">
  <!-- Row 1 -->
  <section class="player tone-purple"><h2 class="player__name">Thomas</h2>
    <svg class="player__dial" viewBox="-55 -55 110 110"><circle class="dial__face" r="50"/><rect class="dial__level" x="-45" y="18" width="90" height="30" clip-path="url(#bowl)"/><circle class="dial__badge" cx="25" cy="-30" r="17"/><text class="dial__text dial__pct" x="25" y="-29">56%</text><use class="dial__heart" href="#heart" x="-52" y="14" width="34" height="31"/><text class="dial__text dial__bpm" x="-35" y="30">160</text></svg></section>
  <section class="player tone-green"><h2 class="player__name">Miller</h2>
    <svg class="player__dial" viewBox="-55 -55 110 110"><circle class="dial__face" r="50"/><rect class="dial__level" x="-45" y="-8" width="90" height="56" clip-path="url(#bowl)"/><circle class="dial__badge" cx="25" cy="-30" r="17"/><text class="dial__text dial__pct" x="25" y="-29">75%</text><use class="dial__heart" href="#heart" x="-52" y="14" width="34" height="31"/><text class="dial__text dial__bpm" x="-35" y="30">145</text></svg></section>
  <section class="player tone-green"><h2 class="player__name">Smith</h2>
    <svg class="player__dial" viewBox="-55 -55 110 110"><circle class="dial__face" r="50"/><rect class="dial__level" x="-45" y="-8" width="90" height="56" clip-path="url(#bowl)"/><circle class="dial__badge" cx="25" cy="-30" r="17"/><text class="dial__text dial__pct" x="25" y="-29">72%</text><use class="dial__heart" href="#heart" x="-52" y="14" width="34" height="31"/><text class="dial__text dial__bpm" x="-35" y="30">149</text></svg></section>
  <section class="player tone-orange"><h2 class="player__name">Davis</h2>
    <svg class="player__dial" viewBox="-55 -55 110 110"><circle class="dial__face" r="50"/><rect class="dial__level" x="-45" y="-10" width="90" height="58" clip-path="url(#bowl)"/><circle class="dial__badge" cx="25" cy="-30" r="17"/><text class="dial__text dial__pct" x="25" y="-29">82%</text><use class="dial__heart" href="#heart" x="-52" y="14" width="34" height="31"/><text class="dial__text dial__bpm" x="-35" y="30">161</text></svg></section>
  <section class="player tone-blue"><h2 class="player__name">Jackson</h2>
    <svg class="player__dial" viewBox="-55 -55 110 110"><circle class="dial__face" r="50"/><rect class="dial__level" x="-45" y="10" width="90" height="38" clip-path="url(#bowl)"/><circle class="dial__badge" cx="25" cy="-30" r="17"/><text class="dial__text dial__pct" x="25" y="-29">82%</text><use class="dial__heart" href="#heart" x="-52" y="14" width="34" height="31"/><text class="dial__text dial__bpm" x="-35" y="30">115</text></svg></section>
  <section class="player tone-orange"><h2 class="player__name">Anderson</h2>
    <svg class="player__dial" viewBox="-55 -55 110 110"><circle class="dial__face" r="50"/><rect class="dial__level" x="-45" y="-10" width="90" height="58" clip-path="url(#bowl)"/><circle class="dial__badge" cx="25" cy="-30" r="17"/><text class="dial__text dial__pct" x="25" y="-29">82%</text><use class="dial__heart" href="#heart" x="-52" y="14" width="34" height="31"/><text class="dial__text dial__bpm" x="-35" y="30">164</text></svg></section>
  <section class="player tone-pink"><h2 class="player__name">Wilson</h2>
    <svg class="player__dial" viewBox="-55 -55 110 110"><circle class="dial__face" r="50"/><rect class="dial__level" x="-45" y="-28" width="90" height="76" clip-path="url(#bowl)"/><circle class="dial__badge" cx="25" cy="-30" r="17"/><text class="dial__text dial__pct" x="25" y="-29">98%</text><use class="dial__heart" href="#heart" x="-52" y="14" width="34" height="31"/><text class="dial__text dial__bpm" x="-35" y="30">186</text></svg></section>

  <!-- Row 2 -->
  <section class="player tone-orange"><h2 class="player__name">Brown</h2>
    <svg class="player__dial" viewBox="-55 -55 110 110"><circle class="dial__face" r="50"/><rect class="dial__level" x="-45" y="-10" width="90" height="58" clip-path="url(#bowl)"/><circle class="dial__badge" cx="25" cy="-30" r="17"/><text class="dial__text dial__pct" x="25" y="-29">82%</text><use class="dial__heart" href="#heart" x="-52" y="14" width="34" height="31"/><text class="dial__text dial__bpm" x="-35" y="30">160</text></svg></section>
  <section class="player tone-green"><h2 class="player__name">Miller</h2>
    <svg class="player__dial" viewBox="-55 -55 110 110"><circle class="dial__face" r="50"/><rect class="dial__level" x="-45" y="-8" width="90" height="56" clip-path="url(#bowl)"/><circle class="dial__badge" cx="25" cy="-30" r="17"/><text class="dial__text dial__pct" x="25" y="-29">75%</text><use class="dial__heart" href="#heart" x="-52" y="14" width="34" height="31"/><text class="dial__text dial__bpm" x="-35" y="30">145</text></svg></section>
  <section class="player tone-green"><h2 class="player__name">Smith</h2>
    <svg class="player__dial" viewBox="-55 -55 110 110"><circle class="dial__face" r="50"/><rect class="dial__level" x="-45" y="-8" width="90" height="56" clip-path="url(#bowl)"/><circle class="dial__badge" cx="25" cy="-30" r="17"/><text class="dial__text dial__pct" x="25" y="-29">72%</text><use class="dial__heart" href="#heart" x="-52" y="14" width="34" height="31"/><text class="dial__text dial__bpm" x="-35" y="30">149</text></svg></section>
  <section class="player tone-orange"><h2 class="player__name">Davis</h2>
    <svg class="player__dial" viewBox="-55 -55 110 110"><circle class="dial__face" r="50"/><rect class="dial__level" x="-45" y="-10" width="90" height="58" clip-path="url(#bowl)"/><circle class="dial__badge" cx="25" cy="-30" r="17"/><text class="dial__text dial__pct" x="25" y="-29">82%</text><use class="dial__heart" href="#heart" x="-52" y="14" width="34" height="31"/><text class="dial__text dial__bpm" x="-35" y="30">161</text></svg></section>
  <section class="player tone-blue"><h2 class="player__name">Jackson</h2>
    <svg class="player__dial" viewBox="-55 -55 110 110"><circle class="dial__face" r="50"/><rect class="dial__level" x="-45" y="10" width="90" height="38" clip-path="url(#bowl)"/><circle class="dial__badge" cx="25" cy="-30" r="17"/><text class="dial__text dial__pct" x="25" y="-29">82%</text><use class="dial__heart" href="#heart" x="-52" y="14" width="34" height="31"/><text class="dial__text dial__bpm" x="-35" y="30">115</text></svg></section>
  <section class="player tone-orange"><h2 class="player__name">Anderson</h2>
    <svg class="player__dial" viewBox="-55 -55 110 110"><circle class="dial__face" r="50"/><rect class="dial__level" x="-45" y="-10" width="90" height="58" clip-path="url(#bowl)"/><circle class="dial__badge" cx="25" cy="-30" r="17"/><text class="dial__text dial__pct" x="25" y="-29">82%</text><use class="dial__heart" href="#heart" x="-52" y="14" width="34" height="31"/><text class="dial__text dial__bpm" x="-35" y="30">164</text></svg></section>
  <section class="player tone-pink"><h2 class="player__name">Wilson</h2>
    <svg class="player__dial" viewBox="-55 -55 110 110"><circle class="dial__face" r="50"/><rect class="dial__level" x="-45" y="-28" width="90" height="76" clip-path="url(#bowl)"/><circle class="dial__badge" cx="25" cy="-30" r="17"/><text class="dial__text dial__pct" x="25" y="-29">98%</text><use class="dial__heart" href="#heart" x="-52" y="14" width="34" height="31"/><text class="dial__text dial__bpm" x="-35" y="30">186</text></svg></section>

  <!-- Row 3 -->
  <section class="player tone-pink"><h2 class="player__name">Wilson</h2>
    <svg class="player__dial" viewBox="-55 -55 110 110"><circle class="dial__face" r="50"/><rect class="dial__level" x="-45" y="-28" width="90" height="76" clip-path="url(#bowl)"/><circle class="dial__badge" cx="25" cy="-30" r="17"/><text class="dial__text dial__pct" x="25" y="-29">98%</text><use class="dial__heart" href="#heart" x="-52" y="14" width="34" height="31"/><text class="dial__text dial__bpm" x="-35" y="30">186</text></svg></section>
  <section class="player tone-green"><h2 class="player__name">Miller</h2>
    <svg class="player__dial" viewBox="-55 -55 110 110"><circle class="dial__face" r="50"/><rect class="dial__level" x="-45" y="-8" width="90" height="56" clip-path="url(#bowl)"/><circle class="dial__badge" cx="25" cy="-30" r="17"/><text class="dial__text dial__pct" x="25" y="-29">75%</text><use class="dial__heart" href="#heart" x="-52" y="14" width="34" height="31"/><text class="dial__text dial__bpm" x="-35" y="30">145</text></svg></section>
  <section class="player tone-green"><h2 class="player__name">Smith</h2>
    <svg class="player__dial" viewBox="-55 -55 110 110"><circle class="dial__face" r="50"/><rect class="dial__level" x="-45" y="-8" width="90" height="56" clip-path="url(#bowl)"/><circle class="dial__badge" cx="25" cy="-30" r="17"/><text class="dial__text dial__pct" x="25" y="-29">72%</text><use class="dial__heart" href="#heart" x="-52" y="14" width="34" height="31"/><text class="dial__text dial__bpm" x="-35" y="30">149</text></svg></section>
  <section class="player tone-orange"><h2 class="player__name">Davis</h2>
    <svg class="player__dial" viewBox="-55 -55 110 110"><circle class="dial__face" r="50"/><rect class="dial__level" x="-45" y="-10" width="90" height="58" clip-path="url(#bowl)"/><circle class="dial__badge" cx="25" cy="-30" r="17"/><text class="dial__text dial__pct" x="25" y="-29">82%</text><use class="dial__heart" href="#heart" x="-52" y="14" width="34" height="31"/><text class="dial__text dial__bpm" x="-35" y="30">161</text></svg></section>
  <section class="player tone-blue"><h2 class="player__name">Jackson</h2>
    <svg class="player__dial" viewBox="-55 -55 110 110"><circle class="dial__face" r="50"/><rect class="dial__level" x="-45" y="10" width="90" height="38" clip-path="url(#bowl)"/><circle class="dial__badge" cx="25" cy="-30" r="17"/><text class="dial__text dial__pct" x="25" y="-29">82%</text><use class="dial__heart" href="#heart" x="-52" y="14" width="34" height="31"/><text class="dial__text dial__bpm" x="-35" y="30">115</text></svg></section>
  <section class="player tone-orange"><h2 class="player__name">Anderson</h2>
    <svg class="player__dial" viewBox="-55 -55 110 110"><circle class="dial__face" r="50"/><rect class="dial__level" x="-45" y="-10" width="90" height="58" clip-path="url(#bowl)"/><circle class="dial__badge" cx="25" cy="-30" r="17"/><text class="dial__text dial__pct" x="25" y="-29">82%</text><use class="dial__heart" href="#heart" x="-52" y="14" width="34" height="31"/><text class="dial__text dial__bpm" x="-35" y="30">164</text></svg></section>
  <section class="player tone-pink"><h2 class="player__name">Wilson</h2>
    <svg class="player__dial" viewBox="-55 -55 110 110"><circle class="dial__face" r="50"/><rect class="dial__level" x="-45" y="-28" width="90" height="76" clip-path="url(#bowl)"/><circle class="dial__badge" cx="25" cy="-30" r="17"/><text class="dial__text dial__pct" x="25" y="-29">98%</text><use class="dial__heart" href="#heart" x="-52" y="14" width="34" height="31"/><text class="dial__text dial__bpm" x="-35" y="30">186</text></svg></section>
</main>
</body>
</html>
```